Business card for a young aspring actress

My daughter is 18 and just starting out on her profession as an actress. She is a member of the Harbour Young Players and has already had some extras work and a featured role in an upcoming Feature film.

She wants/needs a card that she can have to hand to give to those she comes into contact with in the theatre, TV and film industries.

We are thinking that it may be double sided with an impact side including a picture of her and her name etc with the reverse holding contact and other details.

She wants to go by the name Maya Louise Brennick.

She has done a little modelling but sees herself as an actress.

She can be seen in this video
http://www.oakvalepark-academy.org/videos/be0881e4276ee2512c50a07f907c1d03?width=640&height=480

Target Market(s)

Anyone she comes into contact with in theatre TV and film industries.

Industry/Entity Type

Business

Requirements
Nice to have
• She has email and a website www.mayabrennick.com She is quite a connected girl

```html
<!DOCTYPE html>
<html lang="en">
<head>
<meta charset="utf-8">
<title>Maya Louise Brennick – Actress Business Card</title>
<link rel="stylesheet" href="https://fonts.googleapis.com/css2?family=Marcellus&family=Nothing+You+Could+Do&family=Cormorant+Garamond:ital,wght@1,500&display=swap">
<style>
  :root {
    --page: #ffffff;
    --wallpaper-light: #a79f72;
    --wallpaper-dark: #7d754d;
    --door-frame: #ece6c6;
    --door-shadow: #c9c09a;
    --photo-warm: #6e5a48;
    --photo-deep: #2b1f1c;
    --card-cream: #e4e3bd;
    --olive: #7f7e5b;
    --olive-shadow: #5f5e42;
    --label: #7f7e5b;
    --white: #ffffff;
  }
  * { box-sizing: border-box; margin: 0; padding: 0; }
  html, body {
    width: 1200px; height: 1200px; overflow: hidden;
    background: var(--page);
  }
  .card {
    position: absolute;
    left: 120px;
    width: 960px;
    height: 554px;
    overflow: hidden;
  }
  /* Front side */
  .card--front { top: 22px; }
  .wallpaper {
    position: absolute; left: 0; top: 0; width: 454px; height: 100%;
    background: linear-gradient(180deg, var(--wallpaper-dark) 0%, var(--wallpaper-light) 45%, #b3ab80 100%);
  }
  .door-frame {
    position: absolute; left: 454px; top: 0; width: 134px; height: 100%;
    background: linear-gradient(90deg, var(--door-shadow) 0%, var(--door-frame) 18%, #f6f1d8 50%, var(--door-frame) 80%, var(--door-shadow) 100%);
  }
  .portrait {
    position: absolute; left: 588px; top: 0; right: 0; height: 100%;
    background: linear-gradient(135deg, #8f8a70 0%, var(--photo-warm) 40%, var(--photo-deep) 100%);
  }
  .signature-name {
    position: absolute; left: 22px; top: 196px;
    font-family: "Nothing You Could Do", cursive;
    font-weight: 400;
    font-size: 66px; line-height: 96px;
    color: var(--white);
    white-space: nowrap;
  }
  .signature-name span { display: block; }
  .signature-name .surname { padding-left: 14px; }

  /* Back side */
  .card--back { top: 604px; background: var(--card-cream); }
  .title-arc { position: absolute; inset: 0; }
  .contact-labels {
    position: absolute; left: 48px; top: 90px;
    font-family: "Marcellus", serif;
    font-size: 36px; line-height: 50px;
    color: var(--label);
    list-style: none;
    -webkit-text-stroke: 0.6px var(--label);
  }
  .contact-labels .gap { margin-top: 123px; }
  .back-name {
    position: absolute; left: 588px; top: 165px; width: 360px;
    font-family: "Marcellus", serif;
    font-weight: 400;
    font-size: 60px; line-height: 75px;
    color: var(--white);
  }
  .role {
    position: absolute; left: 620px; top: 316px; width: 284px;
    display: flex; align-items: center; justify-content: center; gap: 18px;
    font-family: "Cormorant Garamond", serif;
    font-style: italic; font-weight: 500;
    font-size: 56px;
    color: var(--white);
  }
  .role .tick {
    display: block; width: 18px; height: 4px;
    background: var(--white);
    transform: rotate(-35deg);
  }
</style>
</head>
<body>
  <section class="card card--front" aria-label="Card front">
    <div class="wallpaper" role="img" aria-label="Olive damask wallpaper background"></div>
    <div class="door-frame"></div>
    <div class="portrait" role="img" aria-label="Portrait photo of the actress standing in a doorway"></div>
    <h1 class="signature-name"><span>Maya Louise</span><span class="surname">Brennick</span></h1>
  </section>

  <section class="card card--back" aria-label="Card back">
    <svg class="title-arc" width="960" height="554" viewBox="0 0 960 554" aria-hidden="true">
      <defs>
        <filter id="arc-shadow" x="-20%" y="-20%" width="140%" height="140%">
          <feGaussianBlur stdDeviation="6"/>
        </filter>
      </defs>
      <circle cx="1101" cy="277" r="574" fill="var(--olive-shadow)" opacity="0.35" filter="url(#arc-shadow)"/>
      <circle cx="1097" cy="277" r="569" fill="var(--olive)"/>
    </svg>
    <ul class="contact-labels">
      <li>Phone:</li>
      <li>E-mail:</li>
      <li>Website:</li>
      <li class="gap">Chirplet:</li>
      <li>Circlepage:</li>
    </ul>
    <h2 class="back-name">Maya Louise Brennick</h2>
    <p class="role"><span class="tick"></span>actress<span class="tick"></span></p>
  </section>
</body>
</html>
```